Flyer Design

We are a property company and need attractive flyers that will grab peoples attention. We want them to be bold but simple and not too busy. I attach a draft and also our logo. We will print in A5 size.
Thank you & I look forward to receiving designs.

It Company

```html
<!DOCTYPE html>
<html lang="en">
<head>
<meta charset="utf-8">
<title>Orla Developments Flyer</title>
<link rel="stylesheet" href="https://fonts.googleapis.com/css2?family=Lato:wght@400;700;900&display=swap">
<style>
  :root {
    --page-bg: #f4f5f7;
    --beige: #d3cdbd;
    --wood: #cbbfae;
    --wood-deep: #b7a891;
    --brand-ink: #6b4a33;
    --red: #b43a31;
    --dark-brown: #3b1e15;
    --ink: #141210;
    --white: #ffffff;
  }
  * { box-sizing: border-box; margin: 0; padding: 0; }
  html, body {
    width: 932px; height: 1200px; overflow: hidden;
    background: var(--page-bg);
    font-family: "Lato", Arial, sans-serif;
  }
  .flyer {
    position: absolute; left: 66px; top: 36px;
    width: 800px; height: 1127px;
    background: var(--beige);
    display: flex; flex-direction: column;
  }
  .brand-header {
    height: 195px; position: relative;
  }
  .brand-panel {
    position: absolute; left: 151px; top: 0;
    width: 493px; height: 195px;
    background: linear-gradient(90deg, var(--wood) 0%, #d6ccbc 40%, var(--wood) 70%, var(--wood-deep) 100%);
    display: flex; align-items: flex-end; justify-content: center;
    padding-bottom: 14px;
  }
  .brand-name {
    font-weight: 700; font-size: 40px; letter-spacing: 2px;
    color: var(--brand-ink); text-transform: uppercase;
  }
  .question-band {
    height: 101px; background: var(--red); color: var(--white);
    display: flex; align-items: center; justify-content: center;
    text-align: center; font-weight: 700; font-size: 28px; line-height: 1.3;
  }
  .street-photo {
    height: 471px;
    background: linear-gradient(180deg, #8fb7d6 0%, #b9d1e2 22%, #7d8a80 45%, #3e4a32 72%, #1f2718 100%);
  }
  .struggle-band {
    height: 67px; background: var(--dark-brown); color: var(--white);
    display: flex; align-items: center; justify-content: center;
    font-weight: 700; font-size: 27px;
  }
  .offer {
    flex: 1; display: flex; flex-direction: column; align-items: center;
    text-align: center; color: var(--ink);
    padding-top: 44px;
  }
  .offer-headline {
    font-weight: 700; font-size: 25px; line-height: 1.35;
  }
  .offer-contact {
    margin-top: 40px; font-weight: 700; font-size: 18.5px; line-height: 1.4;
  }
  .web-band {
    height: 74px; background: var(--red); color: var(--white);
    display: flex; align-items: center; justify-content: center;
    font-weight: 700; font-size: 17px; letter-spacing: 2px;
  }
</style>
</head>
<body>
  <main class="flyer">
    <header class="brand-header">
      <div class="brand-panel">
        <span class="brand-name">Orla Developments</span>
      </div>
    </header>
    <section class="question-band">
      <p>Are you a homeowner looking for financial freedom<br>while still keeping your own home?</p>
    </section>
    <div class="street-photo" role="img" aria-label="Photograph of a sunlit street of white weatherboard villas with dark roofs, trees and blue sky"></div>
    <section class="struggle-band">
      <p>Are you struggling to pay your mortgage?</p>
    </section>
    <section class="offer">
      <p class="offer-headline">Orla Developments specialise in subdivisions<br>including finance and management.</p>
      <p class="offer-contact">Call 021 555 014 or email info@orlasubdivisions.com for more information<br>or to find out if your property is suitable for subdivision in Auckland.</p>
    </section>
    <footer class="web-band">
      <p>www.orlasubdivisions.com</p>
    </footer>
  </main>
</body>
</html>
```